Looking for potential sellers

We help people buy and sell homes and are currently looking for potential home sellers. We offer low commissions, are the Local Colorado Springs and Falcon Experts, homes selling fast and at top dollar, Free expert pricing opinions and Consultations, over 9 years of experience, top rated Realtors creative and aggressive marketing strategies. Never merely own a house, THRIVE at Harborview. phone number 482-630-9157 web thriveatharborview.com

```html
<!DOCTYPE html>
<html lang="en">
<head>
<meta charset="utf-8">
<title>Lantern Hill Real Estate – Seller Postcard</title>
<link href="https://fonts.googleapis.com/css2?family=Oswald:wght@400;500&family=Raleway:wght@400;500;600&family=Montserrat:wght@400;600&display=swap" rel="stylesheet">
<style>
  :root{
    --stage:#b9b9b9;
    --ink:#111111;
    --olive:#7d7f2a;
    --olive-dark:#5f6120;
    --olive-light:#9a9b3e;
    --paper:#ffffff;
    --body:#4a4a4a;
    --rule:#3a3a3a;
  }
  *{box-sizing:border-box;margin:0;padding:0}
  html,body{width:1200px;height:890px;overflow:hidden;background:var(--stage)}
  .card{position:absolute;top:33px;width:552px;height:816px;overflow:hidden;box-shadow:0 4px 14px rgba(0,0,0,.35)}
  .front{left:27px;background:var(--ink)}
  .back{left:622px;background:var(--paper)}
  .photo{position:absolute}
  .brand{position:absolute;background:var(--paper);display:flex;align-items:center;justify-content:center;gap:10px;border-bottom:8px solid var(--ink)}
  .brand-name{font-family:'Raleway',sans-serif;font-weight:600;color:var(--olive-dark);text-align:center;line-height:1.15}
  .brand-mark{width:14px;height:14px;background:var(--olive);flex:none}
  .front .brand{left:147px;top:185px;width:258px;height:146px}
  .front .brand-name{font-size:24px}
  .headline-band{position:absolute;left:0;top:493px;width:552px;height:30px;background:var(--olive-dark);opacity:.9}
  .headline{position:absolute;left:124px;top:487px;width:306px;height:42px;background:var(--olive);font-family:'Oswald',sans-serif;font-weight:500;font-size:35px;color:#fff;text-align:center;line-height:42px;letter-spacing:.3px}
  .info{position:absolute;left:0;top:545px;width:552px;height:271px;background:linear-gradient(100deg,var(--olive) 0%,var(--olive-light) 55%,var(--olive) 100%)}
  .intro{position:absolute;left:22px;top:14px;width:508px;font-family:'Raleway',sans-serif;font-size:9.6px;line-height:14.6px;color:#f3f3e6;text-align:center}
  .listings{position:absolute;left:23px;top:102px;list-style:none}
  .listings li{display:flex;align-items:center;gap:8px;height:24.4px;font-family:'Oswald',sans-serif;font-size:9.5px;color:#fff;letter-spacing:.1px}
  .listings svg{width:11px;height:10px;flex:none}
  .web{position:absolute;left:0;top:233px;width:187px;height:16px;background:var(--paper);display:flex;align-items:center;gap:6px;padding-left:23px;font-family:'Montserrat',sans-serif;font-size:9px;letter-spacing:1.5px;color:var(--ink);box-shadow:0 2px 3px rgba(0,0,0,.3)}
  .agent{position:absolute;left:311px;top:648px;width:218px;height:95px;background:var(--paper);border-top:5px solid var(--ink)}
  .agent-photo{position:absolute;left:12px;top:14px;width:72px;height:67px;background:linear-gradient(#9a8f84,#4b4c52)}
  .agent-name{position:absolute;left:96px;top:13px;font-family:'Montserrat',sans-serif;font-weight:600;font-size:14px;color:var(--ink)}
  .agent-role{position:absolute;left:96px;top:30px;width:112px;padding-bottom:3px;border-bottom:1px solid #777;font-family:'Montserrat',sans-serif;font-size:8px;color:#333}
  .agent-tel{position:absolute;left:96px;display:flex;align-items:center;gap:5px;font-family:'Montserrat',sans-serif;font-size:8.4px;color:#333}
  .agent-tel i{display:block;width:9px;height:9px;border-radius:50%;background:var(--olive)}
  .tagline{position:absolute;left:311px;top:749px;width:218px;height:44px;background:var(--ink);color:#fff;font-family:'Oswald',sans-serif;font-size:12.5px;line-height:16px;text-align:center;padding-top:6px;font-variant:small-caps}
  .back-top{position:absolute;left:0;top:0;width:552px;height:363px;background:var(--ink)}
  .back .brand{left:184px;top:123px;width:184px;height:104px;border-bottom-width:6px}
  .back .brand-name{font-size:18px}
  .pitch{position:absolute;left:22px;top:371px;width:508px;font-family:'Raleway',sans-serif;font-size:9px;line-height:14.6px;color:var(--body);text-align:center}
  .stamp{position:absolute;left:23px;top:481px;width:87px;height:87px;border:1.5px solid var(--rule);display:flex;align-items:center;justify-content:center;font-family:'Montserrat',sans-serif;font-size:8.5px;color:var(--ink)}
  .address-line{position:absolute;left:23px;width:506px;height:0;border-top:1.5px solid var(--rule)}
</style>
</head>
<body>

<section class="card front">
  <div class="photo" role="img" aria-label="Pale blue cottage with white porch and metal roof" style="left:23px;top:0;width:248px;height:257px;background:linear-gradient(#6fa3d6 0%,#a9cbd0 40%,#7aa0a2 70%,#5e8a3c 100%)"></div>
  <div class="photo" role="img" aria-label="Yellow house with tiled roof and wisteria" style="left:282px;top:0;width:247px;height:257px;background:linear-gradient(#6e4b3c 0%,#b49a5a 45%,#8c8a52 70%,#6b7a3a 100%)"></div>
  <div class="photo" role="img" aria-label="Modern lit glass home at dusk" style="left:23px;top:266px;width:248px;height:257px;background:linear-gradient(#8f7ea8 0%,#a66f5a 45%,#d39c63 75%,#6c4a33 100%)"></div>
  <div class="photo" role="img" aria-label="Brick and grey siding new-build house" style="left:282px;top:266px;width:247px;height:227px;background:linear-gradient(#5d8fcf 0%,#8d8f95 45%,#7c6a5c 70%,#b39774 100%)"></div>

  <div class="brand"><span class="brand-mark"></span><span class="brand-name">Lantern Hill<br>Real Estate Company</span></div>

  <div class="headline-band"></div>
  <div class="headline">WE’RE HERE TO HELP!</div>

  <div class="info">
    <p class="intro">Lantern Hill Real Estate, and our lead broker Dale Morgan, have been helping clients find their dream home in beautiful Colorado Springs and its surrounding areas since 2009. We know that buying or selling your home can be one of the most exciting (and sometimes trying) times of your life. Because of this, we make a concerted effort to know and understand your wants and needs, which plays a crucial part in both your success, and ours.</p>

    <ul class="listings">
      <li><svg viewBox="0 0 11 10"><path d="M5.5 0 11 5H9.4v5H6.6V7H4.4v3H1.6V5H0z" fill="#fff"/></svg>EXQUISITE, CUSTOM, LUXURY 6 BEDROOM HOME IN BLACK FOREST.</li>
      <li><svg viewBox="0 0 11 10"><path d="M5.5 0 11 5H9.4v5H6.6V7H4.4v3H1.6V5H0z" fill="#fff"/></svg>MODERN BUNGALOW NESTLED DOWNTOWN.</li>
      <li><svg viewBox="0 0 11 10"><path d="M5.5 0 11 5H9.4v5H6.6V7H4.4v3H1.6V5H0z" fill="#fff"/></svg>PANORAMIC VIEWS IN FOUNTAIN.</li>
      <li><svg viewBox="0 0 11 10"><path d="M5.5 0 11 5H9.4v5H6.6V7H4.4v3H1.6V5H0z" fill="#fff"/></svg>BRAND NEW BUILD IN PEYTON.</li>
      <li><svg viewBox="0 0 11 10"><path d="M5.5 0 11 5H9.4v5H6.6V7H4.4v3H1.6V5H0z" fill="#fff"/></svg>IMMACULATE TOWNHOUSE IN SOARING EAGLES.</li>
    </ul>

    <div class="web"><svg width="10" height="10" viewBox="0 0 10 10"><circle cx="5" cy="5" r="4.3" fill="none" stroke="#333" stroke-width="1"/><ellipse cx="5" cy="5" rx="2" ry="4.3" fill="none" stroke="#333" stroke-width=".8"/><path d="M.7 5h8.6" stroke="#333" stroke-width=".8"/></svg>www.thriveatharborview.com</div>
  </div>

  <div class="agent">
    <div class="agent-photo" role="img" aria-label="Portrait of the broker"></div>
    <div class="agent-name">DALE MORGAN</div>
    <div class="agent-role">Employing Broker &amp; Owner</div>
    <div class="agent-tel" style="top:55px"><i></i>482-630-9157</div>
    <div class="agent-tel" style="top:71px"><i></i>482-630-9157</div>
  </div>
  <div class="tagline">Never merely own a house,<br>THRIVE at Harborview!</div>
</section>

<section class="card back">
  <div class="back-top"></div>
  <div class="photo" role="img" aria-label="Stone and siding craftsman home" style="left:23px;top:0;width:249px;height:171px;background:linear-gradient(#5f9ad8 0%,#8d8a78 45%,#6f6452 70%,#b9a27c 100%)"></div>
  <div class="photo" role="img" aria-label="Two-storey home with white garage" style="left:281px;top:0;width:249px;height:171px;background:linear-gradient(#4a6a3a 0%,#4b5563 35%,#b79d80 65%,#d8d8d4 100%)"></div>
  <div class="photo" role="img" aria-label="Large lakeside house among trees" style="left:23px;top:180px;width:249px;height:172px;background:linear-gradient(#3f6a30 0%,#b58b7e 40%,#8a6a58 65%,#6f8a3c 100%)"></div>
  <div class="photo" role="img" aria-label="Blue-grey new-build home under construction" style="left:281px;top:180px;width:249px;height:172px;background:linear-gradient(#4f8fd6 0%,#5b6f8c 45%,#6b7a92 70%,#b0a08a 100%)"></div>

  <div class="brand"><span class="brand-mark"></span><span class="brand-name">Lantern Hill<br>Real Estate Company</span></div>

  <p class="pitch">We help people buy and sell homes and are currently looking for potential home sellers. We offer low commissions, are the Local Colorado Springs and Falcon Experts, homes selling fast and at top dollar, Free expert pricing opinions and Consultations, over 9 years of experience, top rated Realtors creative and aggressive marketing strategies.</p>

  <div class="stamp">STAMP</div>
  <div class="address-line" style="top:605px"></div>
  <div class="address-line" style="top:642px"></div>
  <div class="address-line" style="top:679px"></div>
  <div class="address-line" style="top:716px"></div>
</section>

</body>
</html>
```